Velvet Larks website

Home page and info page design needed
PRODUCTION NOTES

* 10 Page Website
* Blog

CLIENT PURPOSE

• Provide information not easily/commonly available for women over 40
• Focus on unusual opportunities
• Fun / Informative / Unique / Helpful

PLATFORM
Wordpress

SERVICES
Inform / Encourage / Emphasise - Information / Topics etc -
Promote products for the over 40’s - From advertisers etc. -
- -

COMPETITION
Cycle Compass - cyclecompass.co.uk
Kinfolk Hub - kinfolkhub.com
Stay Spry Past Sixty - stayspryspastsixty.com

WEBSITE(S) CLIENT LIKES
kinfolkhub.com
ladytinkerstyle.com
qvn.co.uk
tallowbrook.org.uk

WEBSITE CLIENT DOES NOT LIKE
cyclecompass.co.uk

COMPANY LOGO
Customer has a company logo - their existing site is here http://velvetlarks.com - this is the logo you should use , you need to reflect the feel of the logo throughout the whole design

COLOURS:
as the logo

STRAPLINE:
Dangerously Fascinating Women

EMAIL ADDRESSES TO APPEAR ON WEBSITE:
info@velvetlarks.com -

WEBSITE THEME:
Womens Health

IMAGES THAT BEST REFLECT YOUR COMPANY: •
Retro / Funky / Unusual / Eye-catching• As per original site but more sophisticated•
Focus groups said they liked style/look of old site but thought it looked a bit ‘young’ for target group

HEADER IMAGE:
Women - Active

PAGES:
Home
About Us
Explore Something New
Health & Well Being –
Relationships
Blog
Mind, Body & Soul
Contact

MESSAGE BANNERS:

Need to show recent Blog entries.-Maybe have TOP 5 related issues?
* Boost your sex drive.
* What is HRT? * Suffering from migraines?
* Treatment Options
* Do symptoms get worse when you start on HRT?-Picture of Fenella & Morwen‘ Written by like minded women’
Link to blog entry about the founders of the website?-Maybe a Product option?Advertising option...-Your story..

USER JOURNEYS:

General Service > Land on website > Service Banners > Info Pages > Contact FormQuestions > Land on website > Message Banners > Info Pages > Contact FormContact > Land on website > Clear Telephone / Email Banner > Contact Form

CALL TO ACTION BANNER:

Search the blog..

-

KEYWORDS THAT RELATE TO YOUR BUSINESS:

Menopause
Hormones
Mid Life
Stress
Empty Nest
Womans Health
HRT
Body & Soul
hormone replacement therapy

LOCATION(S):

United Kingdom -

here is the link to the clients current site
http://velvetlarks.com/index.html

Target Market(s)

woman over 40+

Industry/Entity Type

Consulting

Number of Pages Required

1 page

Requirements
Must have
• take the colours and style of the logo and use throughout the design
Should not have
• Cliche pictures of older woman - you need to give the right balance of seriousness and fun - must not come accross as boring BUT also not too light hearted

```html
<!DOCTYPE html>
<html lang="en">
<head>
<meta charset="utf-8">
<title>Velvet Larks – Dangerously Fascinating Women</title>
<link rel="stylesheet" href="https://fonts.googleapis.com/css2?family=Rosarivo&family=Noto+Sans:wght@400;700&family=Oswald:wght@300;500&display=swap">
<style>
:root{
  --magenta:#b4006e;
  --olive:#7b8419;
  --orange:#c76a1e;
  --button:#ff6a00;
  --cream:#fdf5ee;
  --ink:#333;
  --black:#000;
  --yellow:#fde22b;
  --white:#fff;
}
*{margin:0;padding:0;box-sizing:border-box}
html,body{width:920px;height:1200px;overflow:hidden;background:var(--white)}
body{font-family:"Noto Sans",sans-serif;color:var(--ink);position:relative}
.page{position:absolute;left:34px;top:0;width:852px;height:1200px;background:var(--cream);box-shadow:0 0 10px rgba(0,0,0,.25)}
.header{position:absolute;left:9px;top:0;width:834px;height:110px}
.brand{position:absolute;left:20px;top:30px;display:flex;align-items:center;gap:10px}
.brand-dot{width:34px;height:34px;border-radius:50%;background:var(--magenta)}
.brand-name{font-family:"Rosarivo",serif;font-size:28px;line-height:30px;color:var(--magenta);display:block}
.strapline{font-family:"Rosarivo",serif;font-size:11px;color:var(--magenta);display:block;margin-top:2px}
.util-links{position:absolute;right:10px;top:10px;text-align:right;font-size:10px;line-height:15px;font-weight:700}
.util-links a{color:var(--magenta);display:block;text-decoration:underline}
.ad-banner{position:absolute;left:358px;top:45px;width:390px;height:50px;background:linear-gradient(90deg,#c9a07a 0 16%,#5f9a22 16%,#9ccc38)}
.nav{position:absolute;left:9px;top:110px;width:834px;height:37px;background:linear-gradient(#3b3b3b,#202020);display:flex;justify-content:flex-end;align-items:center;padding-right:24px}
.nav a{color:var(--white);font-size:10.5px;font-weight:700;text-decoration:none;padding:0 10px;border-left:1px solid #aaa;line-height:10px}
.nav a:first-child{border-left:0}
.hero{position:absolute;left:9px;top:147px;width:834px;height:181px;background:repeating-linear-gradient(90deg,var(--orange) 0 14px,#bb6018 14px 28px)}
.hero-photo{position:absolute;left:380px;top:0;width:260px;height:181px;background:radial-gradient(ellipse at 55% 45%,#f2d3be,#d59a70 60%,transparent 75%)}
.hero-title{position:absolute;left:18px;top:54px;color:var(--white);font-family:"Oswald",sans-serif;line-height:32px}
.hero-title .lead{font-weight:500;font-size:34px;display:block}
.hero-title .sub{font-weight:300;font-size:30px;display:block}
.search-box{position:absolute;left:632px;top:35px;width:198px;height:114px;background:var(--white);border-radius:3px;padding:10px 12px}
.search-box h3{font-family:"Rosarivo",serif;font-weight:400;color:var(--orange);font-size:17px;border-bottom:1px dotted #999;padding-bottom:2px;width:150px}
.search-box input{margin-top:12px;width:158px;height:19px;border:1px solid #ccc}
.btn{display:inline-block;background:var(--button);color:var(--white);font-size:10.5px;font-weight:700;letter-spacing:.5px;padding:1px 6px;border-radius:2px}
.search-box .btn{margin-top:9px}
.sidebar-box{position:absolute;width:199px;border-radius:6px;padding:8px 9px;color:var(--white)}
.sidebar-box h2{font-family:"Rosarivo",serif;font-weight:400;font-size:20px;margin-bottom:10px}
.sidebar-box p,.sidebar-box li{font-size:11.5px;line-height:15px}
.magenta{background:var(--magenta)}
.olive{background:var(--olive)}
.read-more{display:block;font-family:"Rosarivo",serif;font-size:9px;font-weight:700;color:var(--white);text-decoration:underline;margin:8px 0 0 4px}
.bullets{list-style:none}
.bullets li{padding-left:14px;position:relative;margin-bottom:14px}
.bullets li::before{content:"";position:absolute;left:0;top:5px;width:8px;height:8px;background:var(--white)}
.tags{list-style:none}
.tags li{font-size:10px;line-height:15px;padding-left:15px;position:relative;text-transform:uppercase}
.tags li::before{content:"";position:absolute;left:1px;top:3px;width:8px;height:8px;background:var(--white)}
.article{position:absolute;left:237px;width:385px}
.article h1{font-family:"Rosarivo",serif;font-weight:400;color:var(--magenta);font-size:30px;line-height:30px;margin-bottom:14px}
.article p{font-size:11.5px;line-height:15px}
.article p a{color:var(--ink);text-decoration:underline}
.article .btn{margin-top:10px}
.divider{position:absolute;left:239px;width:380px;border-top:1px dotted #777}
.expert-photo{position:absolute;left:507px;top:823px;width:119px;height:93px;border:1px solid #888;background:linear-gradient(#e8e0cc,#c9b9a0)}
.promo{position:absolute;left:644px;top:516px;width:199px;height:196px;background:linear-gradient(135deg,#e9b39a,#b54a5a)}
.recent{position:absolute;left:644px;top:887px;width:199px;height:52px;border-radius:5px;background:var(--yellow);padding:5px}
.recent span{display:block;height:100%;border-radius:3px;background:linear-gradient(#fff69a,#f7cf00);font-family:"Rosarivo",serif;font-size:20px;color:#222;text-align:center;line-height:42px}
.footer{position:absolute;left:9px;top:1020px;width:834px;height:180px;background:var(--black);color:var(--white)}
.footer-col{position:absolute;top:10px}
.footer-col h4{font-size:13px;font-weight:700;margin-bottom:16px}
.footer-col p,.footer-col li{font-size:8px;line-height:16.5px}
.footer-col ul{list-style:none}
.footer-sep{position:absolute;top:25px;height:155px;border-left:1px dotted #444}
</style>
</head>
<body>
<div class="page">
  <header class="header">
    <div class="brand"><span class="brand-dot"></span><div><span class="brand-name">Velvet Larks</span><span class="strapline">Dangerously Fascinating Women</span></div></div>
    <div class="ad-banner" role="img" aria-label="Advertising banner for KestrelHomes real estate script"></div>
    <div class="util-links"><a>RSS Feed</a><a>Sign Up</a></div>
  </header>

  <nav class="nav">
    <a>Home</a><a>About Us</a><a>Explore Something New</a><a>Health &amp; Well Being</a><a>Relationships</a><a>Blog</a><a>Mind, Body &amp; Soul</a><a>Contact</a>
  </nav>

  <section class="hero">
    <div class="hero-photo" role="img" aria-label="Photo of two smiling women"></div>
    <div class="hero-title"><span class="lead">When you have&nbsp; nished</span><span class="sub">CHANGING, YOUR THROUGH...</span></div>
    <form class="search-box">
      <h3>Blog Search</h3>
      <input type="text" aria-label="Search the blog">
      <div><span class="btn">SEARCH</span></div>
    </form>
  </section>

  <aside class="sidebar-box magenta" style="left:16px;top:352px;height:144px">
    <h2>Your Stories...</h2>
    <p>consectetuer adipiscing elit. Nunc elementum suscipit metusane. Pellentesque tincidunt, ante sed vestibulum laoreet, ipsum diam Aliquam</p>
    <a class="read-more">Read More...</a>
  </aside>
  <aside class="sidebar-box olive" style="left:16px;top:521px;height:144px">
    <h2>New Experiences</h2>
    <p>Women doing amazing things.. lik edriving tanks, sky diving etc.. Pellentesque tincidunt, ante sed vestibulum laoreet, ipsum diam Aliquam</p>
    <a class="read-more">Read More...</a>
  </aside>
  <aside class="sidebar-box magenta" style="left:16px;top:690px;height:244px">
    <h2>Company News</h2>
    <ul class="bullets">
      <li>consectetuer adipiscing elit. Nunc elementum suscipit metusane.</li>
      <li>Pellentesque tincidunt, ante sed vestibulum laoreet, ipsum diam.</li>
      <li>Aliquam vel risusMauri turpis a lorem vehicula vehicula. Etiam porta pur.</li>
    </ul>
    <a class="read-more" style="margin-top:-4px;margin-left:12px">Read More...</a>
  </aside>

  <article class="article" style="top:368px">
    <h1>What is ‘The Menopause’</h1>
    <p>consectetuer adipiscing elit. Nunc elementum suscipit metusane. Pellentesque tincidunt, ante sed vestibulum laoreet, ipsum diam Aliquam vel risusMauri turpis a lorem vehicula vehicula. Etiam porta purus in urna.Sed justo arcu, iaculis vitae,<a>condimentum non, venenatis sit</a> amet, sem.</p>
    <span class="btn">READ MORE</span>
  </article>
  <div class="divider" style="top:537px"></div>

  <article class="article" style="top:566px">
    <h1>HRT - Hormone Replacement Treatment</h1>
    <p>consectetuer adipiscing elit. Nunc elementum suscipit metusane. Pellentesque tincidunt, ante sed vestibulum laoreet, ipsum diam Aliquam vel risusMauri turpis a lorem vehicula vehicula. Etiam porta purus in urna.Sed justo arcu, iaculis vitae,<a>condimentum</a></p>
    <span class="btn" style="margin-top:18px">READ MORE</span>
  </article>
  <div class="divider" style="top:757px"></div>

  <article class="article" style="top:788px;width:260px">
    <h1 style="white-space:nowrap">Ask Our Experts</h1>
    <p>consectetuer adipiscing elit. Nunc elementum suscipit metusane. Pellentesque tincidunt, ante sed vestibulum laoreet, ipsum diam.</p>
    <p style="margin-top:15px">Aliquam vel risusMauri turpis a lorem vehicula vehicula.</p>
  </article>
  <div class="expert-photo" role="img" aria-label="Portrait photo of a health expert"></div>

  <aside class="sidebar-box magenta" style="left:644px;top:352px;height:144px">
    <h2>Tag Cloud</h2>
    <ul class="tags"><li>Menopause</li><li>Hormones</li><li>Mid Life</li><li>Stress</li><li>Empty Nest</li></ul>
  </aside>
  <div class="promo" role="img" aria-label="Advertisement for PoutBloom lip plumper gloss"></div>
  <aside class="sidebar-box olive" style="left:644px;top:741px;height:120px">
    <h2>Blog Categories</h2>
    <ul class="tags"><li>Mind &amp; Body</li><li>Womens Health</li><li>Relationships</li><li>Company News</li></ul>
  </aside>
  <div class="recent"><span>Recent Blog Posts</span></div>

  <footer class="footer">
    <div class="footer-col" style="left:28px;width:270px">
      <h4>See Our Blog Archives</h4>
      <ul>
        <li>* Boost your sex drive.</li>
        <li>* What is HRT?</li>
        <li>* Suffering from migraines?</li>
        <li>* Treatment Options</li>
        <li>* Do symptoms get worse when you start on HRT?-Picture of Fenella &amp; Morwen‘ Written by like minded women’</li>
        <li>Link to blog entry about the founders of the website?-Maybe</li>
      </ul>
    </div>
    <div class="footer-sep" style="left:305px"></div>
    <div class="footer-col" style="left:328px;width:220px">
      <h4>Like to Contact Us</h4>
      <p>Velvet Larks<br>402 W. Larkfield Ave., Suite 7<br>Hollow Bay, NC. 27514</p>
      <p style="margin-top:16px">Phone:&nbsp;&nbsp; (555) 210-4470&nbsp;&nbsp;&nbsp; Fax: (555) 210-4471<br>Email:&nbsp;&nbsp; info@velvetlarks.com</p>
    </div>
    <div class="footer-sep" style="left:560px"></div>
    <div class="footer-col" style="left:584px;width:240px">
      <h4>Send Us Your Stories...</h4>
      <p>Consectetuer adipiscing elit. Nunc elementum suscipit metusane. Pellentesque tincidunt</p>
      <p style="margin-top:14px">ante sed vestibulum laoreet, ipsu dia Aliquam vel risusMauri turpis a lorem vehicula vehicula. Etiam porta purus icon-sectetuer adipiscing elit. Nunc elementum suscipit metusane. Pellentesque tincidunt, ante sed vestibulum laoreet, ipsum</p>
    </div>
  </footer>
</div>
</body>
</html>
```